Brightmoor Card Company Business Cards

We are a trading card store with Zorblix, sports and other TCG cards, we need a business card design that encompasses a clean cut, modern style with a retro flare. website is brightmoorcardco.com for reference. Can utilize a comic book era feel or a more modern outdoor feel to utilize the "Pacific Northwest" elements of tress, mountains, etc.

Industry/Entity Type

Trading cards and collectibles

Contact Information for Business Card

business name, email address, phone number, name, owner job title

Font styles to use
Sans Serif

```html
<!DOCTYPE html>
<html lang="en">
<head>
<meta charset="utf-8">
<title>Brightmoor Card Company – Business Cards</title>
<link href="https://fonts.googleapis.com/css2?family=Montserrat:wght@500;700;800&display=swap" rel="stylesheet">
<style>
  :root {
    --backdrop: #e9e6e1;
    --card-white: #ffffff;
    --card-black: #0d0d0d;
    --accent-cyan: #1fa9dc;
    --accent-grey: #8e9094;
    --ink-dark: #3b3d40;
    --ink-mid: #55585c;
    --logo-grey: #6d7074;
    --logo-light: #b9bcc0;
  }
  * { margin: 0; padding: 0; box-sizing: border-box; }
  html, body { width: 900px; height: 1200px; overflow: hidden; }
  body {
    background: var(--backdrop);
    font-family: "Montserrat", Arial, sans-serif;
    position: relative;
  }
  .card {
    position: absolute;
    left: 114px;
    width: 672px;
    height: 376px;
    border-radius: 22px;
    overflow: hidden;
    box-shadow: 0 10px 24px rgba(0,0,0,0.18);
  }
  .card-front { top: 120px; background: var(--card-white); }
  .card-back { top: 660px; background: var(--card-black); }

  .edge-bands { position: absolute; left: 0; bottom: 0; width: 100%; height: 40px; }

  .brand-mark {
    position: absolute;
    display: flex;
    align-items: center;
    gap: 14px;
  }
  .brand-square { width: 22px; height: 22px; flex: none; }
  .brand-name {
    font-weight: 800;
    text-transform: uppercase;
    line-height: 1.05;
    letter-spacing: 1px;
  }
  .card-front .brand-mark { left: 58px; top: 140px; }
  .card-front .brand-square { background: var(--logo-grey); }
  .card-front .brand-name { color: var(--logo-grey); font-size: 26px; width: 200px; }

  .card-back .brand-mark { left: 50%; top: 50%; transform: translate(-50%, -58%); }
  .card-back .brand-square { background: var(--logo-light); width: 28px; height: 28px; }
  .card-back .brand-name { color: var(--logo-light); font-size: 34px; width: 260px; }

  .divider {
    position: absolute;
    left: 328px; top: 66px;
    width: 2px; height: 218px;
    background: var(--accent-cyan);
  }
  .contact { position: absolute; left: 346px; top: 64px; color: var(--ink-dark); }
  .contact-name { font-size: 31px; font-weight: 700; color: var(--accent-cyan); line-height: 1.1; }
  .contact-role { font-size: 15px; font-weight: 500; color: var(--ink-mid); margin-top: 4px; }
  .contact-address { font-size: 15px; font-weight: 500; line-height: 1.35; margin-top: 26px; }
  .contact-list { list-style: none; margin-top: 8px; }
  .contact-list li {
    display: flex; align-items: center; gap: 10px;
    font-size: 15px; font-weight: 500; line-height: 1.75;
  }
  .contact-icon { width: 15px; height: 15px; flex: none; }
</style>
</head>
<body>

<section class="card card-front" aria-label="Business card front">
  <div class="brand-mark">
    <span class="brand-square"></span>
    <span class="brand-name">Brightmoor Card Company</span>
  </div>

  <div class="divider"></div>

  <div class="contact">
    <p class="contact-name">Dana Whitlock</p>
    <p class="contact-role">Owner</p>
    <p class="contact-address">4820 Cedar Ridge Ave Suite<br>210 Lakewood, Oregon 97035</p>
    <ul class="contact-list">
      <li>
        <svg class="contact-icon" viewBox="0 0 16 16" aria-hidden="true"><path fill="#1fa9dc" d="M3.6 1.2l2.3 2.8-1.3 1.8c.9 2 2.5 3.6 4.6 4.6l1.8-1.3 2.8 2.3-1.3 2.5C7.4 13.6 2.4 8.6 1.1 3.5z"/></svg>
        <span>06-48213579</span>
      </li>
      <li>
        <svg class="contact-icon" viewBox="0 0 16 16" aria-hidden="true"><rect x="1" y="3" width="14" height="10" rx="1.5" fill="#1fa9dc"/><path d="M1.5 4l6.5 5 6.5-5" fill="none" stroke="#fff" stroke-width="1.3"/></svg>
        <span>info@brightmoorcardcompany.com</span>
      </li>
      <li>
        <svg class="contact-icon" viewBox="0 0 16 16" aria-hidden="true"><circle cx="8" cy="8" r="7" fill="#1fa9dc"/><path d="M1 8h14M8 1c-3 3-3 11 0 14M8 1c3 3 3 11 0 14" fill="none" stroke="#fff" stroke-width="1"/></svg>
        <span>www.brightmoorcardcompany.com</span>
      </li>
    </ul>
  </div>

  <svg class="edge-bands" viewBox="0 0 672 40" preserveAspectRatio="none" aria-hidden="true">
    <polygon points="0,26 420,26 432,40 0,40" fill="#1fa9dc"/>
    <polygon points="440,26 672,26 672,40 452,40" fill="#8e9094"/>
  </svg>
</section>

<section class="card card-back" aria-label="Business card back">
  <div class="brand-mark">
    <span class="brand-square"></span>
    <span class="brand-name">Brightmoor Card Company</span>
  </div>

  <svg class="edge-bands" viewBox="0 0 672 40" preserveAspectRatio="none" aria-hidden="true">
    <polygon points="0,28 400,28 410,40 0,40" fill="#1fa9dc"/>
    <polygon points="412,28 672,28 672,40 422,40" fill="#8e9094"/>
  </svg>
</section>

</body>
</html>
```